Best in class business looking for best in class stationery that accurately reflects the brand image we are trying to build as the brand expands throughout the country. The Varying items should be an eye catching design that makes even the simplest letter or small business card stand out in the crowd.

Target Market(s)

Professionals

Industry/Entity Type

Real Estate

Other font styles liked:
• See atttached logo

Requirements
Must have
• Letterhead
• Business cards
• Envelopes
• Labels for larger mailings
Nice to have
• Folders
• Notebook
Should not have
• Stale design elements

```html
<!DOCTYPE html>
<html lang="en">
<head>
<meta charset="utf-8">
<title>Ridgeline Property Group — Stationery</title>
<link href="https://fonts.googleapis.com/css2?family=Cinzel:wght@500&family=Open+Sans:wght@600;700&display=swap" rel="stylesheet">
<style>
:root{
  --navy:#26367a;
  --blue:#2f55a8;
  --ink:#2a3f93;
  --pale:#c0cce3;
  --rule:#5b79bd;
  --paper:#ffffff;
  --backdrop:#e6ebf2;
}
*{margin:0;padding:0;box-sizing:border-box}
html,body{width:1200px;height:800px;overflow:hidden;background:var(--backdrop)}
.canvas{position:relative;width:1200px;height:800px}
.sheet{position:absolute;background:var(--paper);overflow:hidden}
.brand-name{display:block;font-family:"Cinzel",serif;font-weight:500;color:var(--navy);white-space:nowrap;letter-spacing:.02em}
.brand-mark{display:block;background:var(--navy);margin-left:auto;margin-right:auto}
.body-text{font-family:"Open Sans",sans-serif;font-weight:700;color:var(--ink)}
.decor{position:absolute;background:var(--pale)}

/* Letterhead */
.letterhead{left:52px;top:52px;width:488px;height:694px}
.letterhead .brand{position:absolute;left:0;right:0;top:46px;text-align:center}
.letterhead .brand-mark{width:24px;height:24px;margin-bottom:10px}
.letterhead .brand-name{font-size:17px;line-height:20px}
.letterhead .head-rule{position:absolute;left:0;right:0;top:106px;height:1.5px;background:var(--rule)}
.letterhead .decor{left:242px;top:380px;width:246px;height:314px}
.letterhead .contact{position:absolute;left:47px;top:638px;font-size:7.5px;line-height:9px}
.letterhead .contact svg{width:7px;height:7px;vertical-align:-1px;margin-right:3px;fill:var(--ink)}
.letterhead .address{position:absolute;left:307px;top:647px;font-size:7.5px;line-height:9px}

/* Label sheet */
.label-sheet{left:556px;top:52px;width:492px;height:694px}
.label{position:absolute;width:193px;height:128px;border:1px solid #d5dbe8;border-radius:8px;overflow:hidden;background:var(--paper)}
.label .brand{position:absolute;left:0;right:0;top:20px;text-align:center}
.label .brand-mark{width:11px;height:11px;margin-bottom:4px}
.label .brand-name{font-size:9px;line-height:10px}
.label .label-rule{position:absolute;left:0;right:0;top:49px;height:1px;background:var(--rule)}
.label .address{position:absolute;left:0;right:0;top:54px;text-align:center;font-size:5px;line-height:6.5px}
.label .to{position:absolute;left:8px;top:76px;font-size:8px;line-height:10px}
.label .decor{left:134px;top:66px;width:59px;height:62px}
.l1{left:50px;top:75px}.l2{left:251px;top:75px}
.l3{left:50px;top:214px}.l4{left:251px;top:214px}

/* Envelope */
.envelope-back{position:absolute;left:602px;top:400px;width:560px;height:242px;background:var(--navy)}
.envelope-back .flap{position:absolute;left:0;top:0;right:0;height:54px;background:var(--blue);text-align:center;font-size:6.5px;line-height:11px;padding-top:16px}
.envelope-back .flap .body-text{color:#fff;font-weight:600;letter-spacing:.04em}
.envelope-front{left:602px;top:505px;width:512px;height:241px}
.envelope-front .brand{position:absolute;left:4px;top:32px;width:180px;text-align:center}
.envelope-front .brand-mark{width:22px;height:22px;margin-bottom:12px}
.envelope-front .brand-name{font-size:11.5px;line-height:14px}
.envelope-front .decor{left:345px;top:45px;width:167px;height:196px}
</style>
</head>
<body>
<main class="canvas">

  <section class="sheet letterhead" aria-label="Letterhead">
    <div class="brand">
      <span class="brand-mark"></span>
      <span class="brand-name">Ridgeline Property Group</span>
    </div>
    <div class="head-rule"></div>
    <div class="decor" role="img" aria-label="Large faint brand mark decoration"></div>
    <div class="contact body-text">
      <div><svg viewBox="0 0 10 10"><path d="M2 0h2l1 3-1.5 1a6 6 0 0 0 2.5 2.5L7 5l3 1v2c0 1-1 2-2 2A8 8 0 0 1 0 2c0-1 1-2 2-2z"/></svg>0400 218 365</div>
      <div><svg viewBox="0 0 10 10"><path d="M0 2h10v6H0zM0 2l5 3 5-3" stroke="#fff" stroke-width=".8"/></svg>hello@ridgelineproperty.com</div>
      <div><svg viewBox="0 0 10 10"><circle cx="5" cy="5" r="5"/></svg>www.RidgelineProperty.com</div>
    </div>
    <div class="address body-text">42 Harbour Lane, Kew VIC 3101</div>
  </section>

  <section class="sheet label-sheet" aria-label="Mailing label sheet">
    <div class="label l1">
      <div class="brand"><span class="brand-mark"></span><span class="brand-name">Ridgeline Property Group</span></div>
      <div class="label-rule"></div>
      <div class="address body-text">42 Harbour Lane, Kew VIC 3101<br>www.RidgelineProperty.com</div>
      <div class="to body-text">TO:</div>
      <div class="decor" role="img" aria-label="Faint brand mark decoration"></div>
    </div>
    <div class="label l2">
      <div class="brand"><span class="brand-mark"></span><span class="brand-name">Ridgeline Property Group</span></div>
      <div class="label-rule"></div>
      <div class="address body-text">42 Harbour Lane, Kew VIC 3101<br>www.RidgelineProperty.com</div>
      <div class="to body-text">TO:</div>
      <div class="decor" role="img" aria-label="Faint brand mark decoration"></div>
    </div>
    <div class="label l3">
      <div class="brand"><span class="brand-mark"></span><span class="brand-name">Ridgeline Property Group</span></div>
      <div class="label-rule"></div>
      <div class="address body-text">42 Harbour Lane, Kew VIC 3101<br>www.RidgelineProperty.com</div>
      <div class="to body-text">TO:</div>
      <div class="decor" role="img" aria-label="Faint brand mark decoration"></div>
    </div>
    <div class="label l4">
      <div class="brand"><span class="brand-mark"></span><span class="brand-name">Ridgeline Property Group</span></div>
      <div class="label-rule"></div>
      <div class="address body-text">42 Harbour Lane, Kew VIC 3101<br>www.RidgelineProperty.com</div>
      <div class="to body-text">TO:</div>
      <div class="decor" role="img" aria-label="Faint brand mark decoration"></div>
    </div>
  </section>

  <section class="envelope-back" aria-label="Envelope back">
    <div class="flap">
      <div class="body-text">www.RidgelineProperty.com</div>
      <div class="body-text">42 Harbour Lane, Kew VIC 3101</div>
    </div>
  </section>

  <section class="sheet envelope-front" aria-label="Envelope front">
    <div class="brand"><span class="brand-mark"></span><span class="brand-name">Ridgeline Property Group</span></div>
    <div class="decor" role="img" aria-label="Large faint brand mark decoration"></div>
  </section>

</main>
</body>
</html>
```